Fishing charter business in Sitka Alaska needs new business card design

I have had the same design for 10 plus years, ready for something different. I have attached a copy of my current card and my website link is www.bluecoveangling.net
I am looking for something that will catch my clients eye, although I rely on word of mouth for most of my business a a nice business card will help people remember who I am. My business is located in Sitka Alaska, there are probably 20-30 other charter businesses in Sitka. I like the way my current card is laid out, with the two tone black and grey. I can leave it up to the designers to come up with something else.
Target Market(s)
men, women, couples. Anyone who likes fishing
Industry/Entity Type
Tourism
Contact Information for Business Card
Dorrance's Charter Service
Tidewater Rockline Sportfishing
Colors
Designer to choose colors to be used in the design.
Requirements
Must have
- Gilbert Dorrance
- PO Box 4716
- Kelso Cove, AK 99901
- Compass Rose image
- 100 Ton USCG Licensed Captain
- gdorrance@wavelink.net
- 907-555-0142
- www.bluecoveangling.net
Nice to have
- ghost image of "boat helm"
Should not have
- be to complex

```html
<!DOCTYPE html>
<html lang="en">
<head>
<meta charset="utf-8">
<title>Gilbert Dorrance – Business Card</title>
<link href="https://fonts.googleapis.com/css2?family=Oswald:wght@600&family=Lato:wght@400&family=Montserrat:wght@700&display=swap" rel="stylesheet">
<style>
  :root {
    --page-bg: #9aaeb2;
    --card-bg: #bfd5d8;
    --navy: #14314a;
    --ink: #1d3346;
    --accent: #e8532b;
    --ghost: #8f9fa4;
  }
  * { margin: 0; padding: 0; box-sizing: border-box; }
  html, body {
    width: 1200px;
    height: 1200px;
    overflow: hidden;
    background: var(--page-bg);
  }
  .card {
    position: absolute;
    left: 50px;
    top: 286px;
    width: 1100px;
    height: 628px;
    background: var(--card-bg);
  }
  .helm-ghost {
    position: absolute;
    left: 118px;
    top: 88px;
    width: 198px;
    height: 198px;
    border-radius: 50%;
    background: var(--ghost);
    opacity: 0.55;
  }
  .identity {
    position: absolute;
    left: 59px;
    top: 140px;
  }
  .identity__name {
    font-family: "Oswald", sans-serif;
    font-weight: 600;
    font-size: 44px;
    line-height: 1;
    letter-spacing: 0.5px;
    color: var(--navy);
    text-transform: uppercase;
  }
  .identity__title {
    font-family: "Lato", sans-serif;
    font-size: 23px;
    color: var(--accent);
    margin-top: 4px;
  }
  .contacts {
    position: absolute;
    left: 72px;
    top: 437px;
    list-style: none;
    font-family: "Lato", sans-serif;
    font-size: 24px;
    color: var(--ink);
  }
  .contacts li {
    display: flex;
    align-items: center;
    height: 27px;
    white-space: nowrap;
  }
  .contacts svg {
    width: 18px;
    height: 18px;
    margin-right: 10px;
    flex: none;
    fill: var(--accent);
  }
  .compass {
    position: absolute;
    left: 593px;
    top: 151px;
    width: 350px;
    height: 350px;
    border-radius: 50%;
    background: var(--navy);
  }
  .cardinal {
    position: absolute;
    font-family: "Montserrat", sans-serif;
    font-weight: 700;
    font-size: 29px;
    color: var(--ink);
    transform: translate(-50%, -50%);
  }
  .cardinal--n { left: 768px; top: 84px; }
  .cardinal--s { left: 768px; top: 568px; }
  .cardinal--w { left: 525px; top: 326px; }
  .cardinal--e { left: 1015px; top: 326px; }
</style>
</head>
<body>
  <div class="card">
    <div class="helm-ghost" role="img" aria-label="Faint ghost image of a boat helm wheel"></div>

    <div class="identity">
      <h1 class="identity__name">Gilbert Dorrance</h1>
      <p class="identity__title">100 Ton USCG Licensed Captain</p>
    </div>

    <ul class="contacts">
      <li>
        <svg viewBox="0 0 24 24" aria-hidden="true"><path d="M6.6 10.8a15.1 15.1 0 0 0 6.6 6.6l2.2-2.2a1 1 0 0 1 1-.25 11.4 11.4 0 0 0 3.6.57 1 1 0 0 1 1 1V20a1 1 0 0 1-1 1A17 17 0 0 1 3 4a1 1 0 0 1 1-1h3.5a1 1 0 0 1 1 1c0 1.25.2 2.450.57 3.57a1 1 0 0 1-.25 1z"/></svg>
        +907-555-0142
      </li>
      <li>
        <svg viewBox="0 0 24 24" aria-hidden="true"><path d="M2 5h20v14H2z M3 6l9 7 9-7" stroke="#bfd5d8" stroke-width="1.5"/></svg>
        gdorrance@wavelink.net
      </li>
      <li>
        <svg viewBox="0 0 24 24" aria-hidden="true"><circle cx="12" cy="12" r="10"/><path d="M2 12h20M12 2c3 3 3 17 0 20M12 2c-3 3-3 17 0 20M4 7h16M4 17h16" fill="none" stroke="#bfd5d8" stroke-width="1.2"/></svg>
        www.bluecoveangling.net
      </li>
      <li>
        <svg viewBox="0 0 24 24" aria-hidden="true"><path d="M12 2a7 7 0 0 0-7 7c0 5 7 13 7 13s7-8 7-13a7 7 0 0 0-7-7zm0 9.5a2.5 2.5 0 1 1 0-5 2.5 2.5 0 0 1 0 5z"/></svg>
        P.O. Box 4716. Kelso Cove, AK 99901
      </li>
    </ul>

    <div class="compass" role="img" aria-label="Compass rose illustration in navy"></div>
    <span class="cardinal cardinal--n">N</span>
    <span class="cardinal cardinal--s">S</span>
    <span class="cardinal cardinal--w">W</span>
    <span class="cardinal cardinal--e">E</span>
  </div>
</body>
</html>
```